Law Firm Advertising Design Needed

Law Office of Dorvel K Tansy provides legal services to businesses and individuals who have been or are being injured. Our main practice area is personal injury (car accidents, wrongful death, premises liability), but we are looking for an ad that highlights a lesser known area of our practice - insurance company bad faith and breach of contract.

This ad will be placed in 8 1/2" x 11" format in a local neighborhood directory. It will also be placed in a smaller format (to be determined) in the local newspaper of a region of Arizona that has recently lost a considerable number of homes and people to wildfire.

We want to convey through the ad that our firm is available to help if their insurance company is not paying a legitimate claim or not paying enough for their claim.

Because of the tragic nature of the events in Yarnell, we would like to avoid images of fire or anything resembling fire. However, the ad should capture the attention of individuals who are struggling through an insurance claim with all the stacks of paperwork and frustrated with unresponsive adjusters and unreasonably low offers.

The design should convey a feeling of safety, security and being taken care of.

Information that must be included in the ad are: the firm name (Law Office of Dorvel K Tansy), address (4857 W 17th Avenue, Ste 406, Phoenix, AZ 85033), the phone number (602-574-2930) and the fact that we have mobile offices available to assist in your area.

An example of text that has been used in the past is here:
"If your own insurance company is refusing to pay what you are owed on a claim, call the Law Office of Dorvel K Tansy. We fight for you by examining the reasons your insurance carrier is denying or making an insufficient offer on the claim; updating and correcting claim documentation; making a new demand and filing a lawsuit if necessary. Whether it's a simple misunderstanding or something more complicated, we can help!

Here are a few of the kinds of claims we handle:
- Hit and Run or Uninsured driver claims
- Fire, flood and property loss
- Life insurance benefits
- Health insurance claims
- Catastrophic losses
- Business insurance
- Wrongful Death Benefits

Our attorneys are available to help you cut through the nonsense. Call to make an appointment for a free consultation with an attorney today. "

An example of a previous ad for car accident services is attached for reference.
Updates

Hi Everyone,

The main lawyer involved in the decision making process has been giving me some feedback in general on the designs that I thought I would pass along.  He does not want the name of the law firm to be the first thing you notice when you look at the ad. Try to keep that small and possibly to the bottom of the ad. The phone number should be rather large, but the address should be rather small (we are required by the State Bar to include our address, but we don't want our location to limit the location of our clients because our mobile offices can travel to them).  He would prefer that the logo either not be included or be not a significant part of the ad.

                                   

Thanks!  I will continue providing individual feedback to ads received. 

Target Market(s)

Low to middle income residents of the State of Arizona with little or no college education

Industry/Entity Type

Insurance

```html
<!DOCTYPE html>
<html lang="en">
<head>
<meta charset="utf-8">
<title>Law Office of Dorvel K Tansy – Insurance Claims Ad</title>
<link rel="stylesheet" href="https://fonts.googleapis.com/css2?family=Libre+Baskerville:wght@700&family=Tinos:wght@400;700&family=Cinzel:wght@400&display=swap">
<style>
  :root {
    --ink: #000000;
    --paper: #ffffff;
    --navy: #0b3270;
    --navy-band: #0a2f6b;
    --haze: rgba(150, 175, 215, 0.28);
    --title-shadow: #8a8a8a;
    --photo-dark: #1a1410;
    --photo-mid: #3a2c22;
    --photo-warm: #6b3a2a;
  }
  html, body {
    margin: 0;
    padding: 0;
    width: 1200px;
    height: 1000px;
    overflow: hidden;
    background: var(--paper);
  }
  .ad {
    position: relative;
    width: 1200px;
    height: 1000px;
    background: var(--paper);
    font-family: "Tinos", "Times New Roman", serif;
  }
  .rule-band {
    position: absolute;
    left: 236px;
    width: 760px;
    height: 22px;
    box-sizing: border-box;
    border: 5px solid var(--ink);
    background: var(--navy-band);
  }
  .rule-band--top { top: 8px; }
  .rule-band--bottom { top: 969px; }

  .firm-title {
    position: absolute;
    top: 34px;
    left: 236px;
    width: 760px;
    margin: 0;
    text-align: center;
    font-family: "Libre Baskerville", "Times New Roman", serif;
    font-weight: 700;
    font-size: 48px;
    line-height: 53px;
    letter-spacing: 1px;
    color: var(--paper);
    -webkit-text-stroke: 1.5px var(--ink);
    text-shadow: -3px 3px 0 var(--title-shadow), -4px 4px 3px rgba(0,0,0,0.35);
  }

  .panel {
    position: absolute;
    top: 198px;
    left: 236px;
    width: 760px;
    height: 706px;
    box-sizing: border-box;
    border: 7px solid var(--ink);
    background: var(--navy);
    overflow: hidden;
  }
  .panel__statue {
    position: absolute;
    left: 330px;
    top: 2px;
    width: 200px;
    height: 690px;
    background: radial-gradient(ellipse at 50% 40%, var(--haze) 0%, rgba(150,175,215,0.12) 55%, rgba(150,175,215,0) 75%);
  }
  .portrait {
    position: absolute;
    left: 50px;
    top: 22px;
    width: 284px;
    height: 369px;
    background:
      radial-gradient(ellipse at 20% 55%, var(--photo-warm) 0%, rgba(107,58,42,0) 35%),
      radial-gradient(ellipse at 65% 55%, #2c3446 0%, rgba(44,52,70,0) 45%),
      linear-gradient(180deg, var(--photo-mid) 0%, var(--photo-dark) 100%);
    box-shadow: 0 0 14px 4px rgba(0,0,0,0.55);
  }
  .portrait__tagline {
    position: absolute;
    left: 17px;
    top: 222px;
    margin: 0;
    font-family: "Cinzel", "Times New Roman", serif;
    font-size: 13.5px;
    line-height: 26px;
    color: var(--paper);
    letter-spacing: 0.3px;
  }
  .pitch {
    position: absolute;
    left: 385px;
    top: 30px;
    width: 350px;
    margin: 0;
    text-align: center;
    text-transform: uppercase;
    font-size: 14.3px;
    line-height: 17.7px;
    color: var(--paper);
    text-shadow: 1px 1px 1px rgba(0,0,0,0.6);
  }
  .claims {
    position: absolute;
    left: 0;
    top: 402px;
    width: 746px;
    margin: 0;
    padding: 0;
    list-style: none;
    text-align: center;
    text-transform: uppercase;
    font-size: 18px;
    line-height: 21px;
    color: var(--paper);
    text-shadow: 1px 1px 1px rgba(0,0,0,0.6);
  }
  .closing {
    position: absolute;
    left: 40px;
    top: 491px;
    width: 660px;
    margin: 0;
    text-align: center;
    text-transform: uppercase;
    font-size: 15.3px;
    line-height: 18.5px;
    color: var(--paper);
    text-shadow: 1px 1px 1px rgba(0,0,0,0.6);
  }
  .brand {
    position: absolute;
    left: 0;
    top: 602px;
    width: 746px;
    display: flex;
    justify-content: center;
    align-items: center;
    gap: 12px;
  }
  .brand__mark {
    width: 26px;
    height: 26px;
    background: var(--paper);
  }
  .brand__name {
    font-size: 34px;
    color: var(--paper);
  }

  .contact {
    position: absolute;
    left: 236px;
    width: 760px;
    text-align: center;
    margin: 0;
    color: var(--ink);
  }
  .contact__address {
    top: 908px;
    font-size: 17px;
    font-weight: 700;
    line-height: 20px;
    letter-spacing: 0.2px;
  }
  .contact__phone {
    top: 927px;
    font-size: 33px;
    font-weight: 700;
    line-height: 38px;
  }
</style>
</head>
<body>
<main class="ad">
  <div class="rule-band rule-band--top"></div>

  <h1 class="firm-title">LAW OFFICE<br>OF<br>DORVEL K. TANSY</h1>

  <section class="panel">
    <div class="panel__statue" role="img" aria-label="Faint figure of Lady Justice holding scales"></div>

    <div class="portrait" role="img" aria-label="Portrait of the attorney in a dark suit seated at his desk with a framed diploma behind">
      <p class="portrait__tagline">Any Accident,<br>Any Injury…<br>Let us fight for you!</p>
    </div>

    <p class="pitch">"If your own insurance company<br>is refusing to pay what<br>you are owed on a claim,<br>call the Law Office of<br>Dorvel K Tansy.<br>We fight for you<br>by examining the reasons<br>your insurance carrier<br>is denying or<br>making an insufficient offer<br>on the claim;<br>updating<br>and correcting claim<br>documentation;<br>making a new demand and<br>filing a lawsuit<br>if necessary. Whether it's a<br>simple misunderstanding<br>or something more complicated,<br>we can help!"</p>

    <ul class="claims">
      <li>- Hit and Run or Uninsured Driver Claims- Fire, Flood and Property Loss</li>
      <li>- Life Insurance Benefits- Health Insurance Claims</li>
      <li>- Catastrophic Losses- Business Insurance</li>
      <li>- Wrongful Death Benefits</li>
    </ul>

    <p class="closing">“ Our attorneys are available to help you cut through the nonsense.<br>Call to make an appointment or look for our mobile offices for<br>a free consultation with an attorney today. "</p>

    <div class="brand">
      <span class="brand__mark"></span>
      <span class="brand__name">Tansy Law</span>
    </div>
  </section>

  <p class="contact contact__address">4857 W 17TH AVENUE, STE 406, PHOENIX, AZ 85033</p>
  <p class="contact contact__phone">602-574-2930</p>

  <div class="rule-band rule-band--bottom"></div>
</main>
</body>
</html>
```